M25 Billboard Advert Required Please

I need an advert for a motorway Billboard on the M25 , the advert should show the following in big letters:
GUTTER CLEANING
TOMSDRAINWORKS.NET and a small logo off to the side (Our logo is attached)

The printer has requested the following (Important please) the advert has to be
pdf file / 300 dpi/landscape orientation / scaled to a minimum 25% advert size ( this particular site is 22ft x 10ft so 25% of this please). Please also make sure that the artwork is embedded and outlined correctly if this is incorrect it will affect the printing of the banner.
Updates

Need extra days to review

Target Market(s)

General Public

Industry/Entity Type

Gutter Cleaning

Requirements
Should not have
• No Change to our Logo

```html
<!DOCTYPE html>
<html lang="en">
<head>
<meta charset="utf-8">
<title>Tom's Drainworks – Motorway Billboard</title>
<link rel="stylesheet" href="https://fonts.googleapis.com/css2?family=Anton&family=Archivo+Black&family=Open+Sans:wght@600&display=swap">
<style>
  :root {
    --page-bg: #ffffff;
    --board-bg: #ffffff;
    --red-deep: #3a0003;
    --red-mid: #8e0810;
    --red-bright: #e31b23;
    --headline-red: #b8202a;
    --ink: #0a0a0a;
  }
  html, body {
    margin: 0;
    padding: 0;
    width: 866px;
    height: 1200px;
    overflow: hidden;
    background: var(--page-bg);
  }
  .canvas {
    position: relative;
    width: 866px;
    height: 1200px;
  }
  .billboard {
    position: absolute;
    left: 33px;
    top: 418px;
    width: 800px;
    height: 364px;
    background: var(--board-bg);
    box-shadow: 0 6px 12px rgba(0, 0, 0, 0.35);
  }
  .billboard svg {
    display: block;
  }
  .headline {
    font-family: "Anton", "Impact", sans-serif;
    fill: var(--headline-red);
  }
  .web-address {
    font-family: "Archivo Black", "Arial Black", sans-serif;
    fill: var(--ink);
  }
  .brand-name {
    font-family: "Anton", "Impact", sans-serif;
    fill: var(--ink);
  }
  .brand-tagline {
    font-family: "Open Sans", Arial, sans-serif;
    font-weight: 600;
    fill: var(--ink);
  }
</style>
</head>
<body>
<main class="canvas">
  <section class="billboard" aria-label="Gutter cleaning billboard">
    <svg width="800" height="364" viewBox="0 0 800 364" xmlns="http://www.w3.org/2000/svg">
      <defs>
        <linearGradient id="band-top-fill" x1="0" y1="0" x2="1" y2="0">
          <stop offset="0" stop-color="var(--red-deep)"/>
          <stop offset="0.55" stop-color="var(--red-mid)"/>
          <stop offset="1" stop-color="var(--red-bright)"/>
        </linearGradient>
        <linearGradient id="band-bottom-fill" x1="0" y1="0" x2="0" y2="1">
          <stop offset="0" stop-color="#c8141c"/>
          <stop offset="1" stop-color="#7a0208"/>
        </linearGradient>
      </defs>

      <polygon class="band-top" points="0,0 800,0 800,44 400,22 0,44" fill="url(#band-top-fill)"/>
      <polygon class="band-bottom" points="0,320 400,341 800,320 800,364 0,364" fill="url(#band-bottom-fill)"/>

      <text class="headline" x="48" y="212" font-size="159" textLength="721" lengthAdjust="spacingAndGlyphs">GUTTER CLEANING?</text>

      <line class="divider" x1="119" y1="233" x2="696" y2="233" stroke="var(--ink)" stroke-width="4" stroke-linecap="round"/>

      <g class="brand">
        <rect class="brand-mark" x="76" y="267" width="9" height="9" fill="var(--headline-red)"/>
        <text class="brand-name" x="90" y="277" font-size="14" textLength="97" lengthAdjust="spacingAndGlyphs">Tom's Drainworks</text>
        <text class="brand-tagline" x="76" y="290" font-size="6.2" textLength="111" lengthAdjust="spacingAndGlyphs">Clear drains keep your home safe</text>
      </g>

      <text class="web-address" x="208" y="289" font-size="45" textLength="519" lengthAdjust="spacingAndGlyphs">TOMSDRAINWORKS.NET</text>
    </svg>
  </section>
</main>
</body>
</html>
```